Business Card Design

We need a business card design for a Executive search firm based in London & the North East called Kestrelby. We specialise in mid - snr level (£50k - £200k) IT placements. Our company colour is navy blue.

Target Market(s)

CEO, HR Director, Sales Director/VP - (35 - 50), well educated, British, European & American

Industry/Entity Type

Business

Contact Information for Business Card

Kestrelby Staffing Limited, Owen Caskell
Mobile - 0044 7731 482 616
London Office - Kestrelby House, 27 Fernmoor, Wexcombe. HA5 3LQ
Tel: 00 44 20 418 62093
North East Office – Velmora Centre, Ashgrove Way, Tillerby, NE41 2RD
Tel: 00 44 191 6842051
www.kestrelbystaffing-example.com

Also the same details for my Business Partner Ravi Tolani
with his mobile number as 0044 7852 307718

Requirements
Must have
• must have the same logo

the logo needs to be the same but made sharper

```html
<!DOCTYPE html>
<html lang="en">
<head>
<meta charset="UTF-8">
<title>Kestrelby Staffing – Business Cards</title>
<link href="https://fonts.googleapis.com/css2?family=Arimo:wght@400;700&display=swap" rel="stylesheet">
<style>
  :root {
    --page: #eef0f2;
    --card-white: #ffffff;
    --brand-navy: #1b5b80;
    --ink-navy: #1e5d84;
    --ink-soft: #3f6f8f;
    --rule: #9fb4c3;
    --on-navy: #e9f0f5;
  }
  * { margin: 0; padding: 0; box-sizing: border-box; }
  html, body {
    width: 1200px;
    height: 900px;
    overflow: hidden;
    background: var(--page);
    font-family: "Arimo", Arial, sans-serif;
  }
  .card-sheet {
    width: 1200px;
    height: 900px;
    display: grid;
    grid-template-columns: 520px 520px;
    grid-template-rows: 316px 316px;
    column-gap: 60px;
    row-gap: 52px;
    justify-content: center;
    align-content: center;
  }
  .card {
    width: 520px;
    height: 316px;
    border-radius: 4px;
    box-shadow: 0 2px 10px rgba(20, 40, 60, 0.12);
    position: relative;
  }
  .card-back {
    grid-column: 1 / span 2;
    justify-self: center;
  }

  /* Company name */
  .company-name {
    font-weight: 700;
    letter-spacing: 0.01em;
  }

  /* Front */
  .card-front {
    background: var(--card-white);
    color: var(--ink-navy);
  }
  .card-front .company-name {
    position: absolute;
    top: 30px;
    right: 36px;
    font-size: 26px;
    color: var(--brand-navy);
  }
  .holder {
    position: absolute;
    top: 56px;
    left: 36px;
  }
  .holder-name {
    font-size: 17px;
    font-weight: 700;
    letter-spacing: 0.02em;
    text-transform: uppercase;
  }
  .holder-title {
    font-size: 13px;
    margin-top: 3px;
    color: var(--ink-soft);
  }
  .holder-mobile {
    font-size: 12.5px;
    margin-top: 12px;
  }
  .offices {
    position: absolute;
    right: 36px;
    bottom: 58px;
    display: flex;
    align-items: stretch;
    font-size: 12px;
    line-height: 1.45;
  }
  .office { padding: 0 14px; }
  .office-london { text-align: right; }
  .office-northeast { text-align: left; padding-right: 0; }
  .office-divider {
    width: 1px;
    background: var(--rule);
  }
  .office-label {
    font-weight: 700;
    text-decoration: underline;
    margin-bottom: 2px;
  }
  .office-tel {
    display: inline-flex;
    align-items: center;
    gap: 5px;
  }
  .office-tel svg { width: 10px; height: 10px; fill: var(--ink-navy); }
  .website {
    position: absolute;
    right: 36px;
    bottom: 26px;
    font-size: 11.5px;
    color: var(--ink-soft);
  }

  /* Back */
  .card-back {
    background: var(--brand-navy);
    display: flex;
    align-items: center;
    justify-content: center;
  }
  .card-back .company-name {
    font-size: 46px;
    color: var(--on-navy);
  }
</style>
</head>
<body>
<main class="card-sheet">

  <section class="card card-front" aria-label="Business card front, Owen Caskell">
    <p class="company-name">Kestrelby</p>
    <div class="holder">
      <p class="holder-name">Owen Caskell</p>
      <p class="holder-title">President</p>
      <p class="holder-mobile">0044 7731 482 616</p>
    </div>
    <div class="offices">
      <div class="office office-london">
        <p class="office-label">London Office</p>
        <p>Kestrelby House, 27 Fernmoor,</p>
        <p>Wexcombe. HA5 3LQ</p>
        <p class="office-tel">00 44 20 418 62093
          <svg viewBox="0 0 10 10" aria-hidden="true"><path d="M2 0.5 L3.6 0.5 L4.3 2.8 L3.2 3.6 C3.8 5 5 6.2 6.4 6.8 L7.2 5.7 L9.5 6.4 L9.5 8 C9.5 8.9 8.9 9.5 8 9.5 C4 9.2 0.8 6 0.5 2 C0.5 1.1 1.1 0.5 2 0.5 Z"/></svg>
        </p>
      </div>
      <div class="office-divider"></div>
      <div class="office office-northeast">
        <p class="office-label">North East Office</p>
        <p>Velmora Centre, Ashgrove</p>
        <p>Way, Tillerby, NE41 2RD</p>
        <p class="office-tel">
          <svg viewBox="0 0 10 10" aria-hidden="true"><path d="M2 0.5 L3.6 0.5 L4.3 2.8 L3.2 3.6 C3.8 5 5 6.2 6.4 6.8 L7.2 5.7 L9.5 6.4 L9.5 8 C9.5 8.9 8.9 9.5 8 9.5 C4 9.2 0.8 6 0.5 2 C0.5 1.1 1.1 0.5 2 0.5 Z"/></svg>
          00 44 191 6842051</p>
      </div>
    </div>
    <p class="website">www.kestrelbystaffing-example.com</p>
  </section>

  <section class="card card-front" aria-label="Business card front, Ravi Tolani">
    <p class="company-name">Kestrelby</p>
    <div class="holder">
      <p class="holder-name">Ravi Tolani</p>
      <p class="holder-title">President</p>
      <p class="holder-mobile">0044 7852 307718</p>
    </div>
    <div class="offices">
      <div class="office office-london">
        <p class="office-label">London Office</p>
        <p>Kestrelby House, 27 Fernmoor,</p>
        <p>Wexcombe. HA5 3LQ</p>
        <p class="office-tel">00 44 20 418 62093
          <svg viewBox="0 0 10 10" aria-hidden="true"><path d="M2 0.5 L3.6 0.5 L4.3 2.8 L3.2 3.6 C3.8 5 5 6.2 6.4 6.8 L7.2 5.7 L9.5 6.4 L9.5 8 C9.5 8.9 8.9 9.5 8 9.5 C4 9.2 0.8 6 0.5 2 C0.5 1.1 1.1 0.5 2 0.5 Z"/></svg>
        </p>
      </div>
      <div class="office-divider"></div>
      <div class="office office-northeast">
        <p class="office-label">North East Office</p>
        <p>Velmora Centre, Ashgrove</p>
        <p>Way, Tillerby, NE41 2RD</p>
        <p class="office-tel">
          <svg viewBox="0 0 10 10" aria-hidden="true"><path d="M2 0.5 L3.6 0.5 L4.3 2.8 L3.2 3.6 C3.8 5 5 6.2 6.4 6.8 L7.2 5.7 L9.5 6.4 L9.5 8 C9.5 8.9 8.9 9.5 8 9.5 C4 9.2 0.8 6 0.5 2 C0.5 1.1 1.1 0.5 2 0.5 Z"/></svg>
          00 44 191 6842051</p>
      </div>
    </div>
    <p class="website">www.kestrelbystaffing-example.com</p>
  </section>

  <section class="card card-back" aria-label="Business card back">
    <p class="company-name">Kestrelby</p>
  </section>

</main>
</body>
</html>
```